Curl Radiant through and through. Hair stylist that specializes in extensions.

I am Marisol I am a hair stylist and I would like a website designed for my hair business.

I currently book clients via my profile on trimnook.example/marisolbrantley

I need a professional website ( curlradiantthroughandthrough.example ) to display photos and prices for services offered.

I would like to have a home page with a brief bio, Image with logo and testimonials at the bottom, and a header with tab that include: menu of services, gallery,and FAQs.

On the "Services" page, I'm not interested in photos on this page. Just the name of the service, brief description, and pricing. I would also like to have, on this page, "Appointment Request" with fields that include: Name, service requested, desired time frame (morning, afternoon, evening), and contact number and email

On the "Gallery" page, I would like pictures only, but arranged and/or presented in a creative way...

Target Market(s)

Women ages 25-55 who interested in hair extension services.

Industry/Entity Type

Hair And Beauty

Coding

Number of Pages Required

5+ page

Font styles to use
Sans Serif

Requirements
Must have
• Must include tabs that include, Menu of services offered, a quick fund link to pay deposits with ease, location, contact information, photo gallery, and policy/faqs.
Nice to have
• If possible i would like to stream music with the ability to be silenced. I would like a neutral color palette tans and beige.
Should not have
• stock images

```html
<!DOCTYPE html>
<html lang="en">
<head>
<meta charset="utf-8">
<title>Curl Radiant through and through</title>
<link href="https://fonts.googleapis.com/css2?family=Archivo+Black&family=Arimo:wght@400;700&family=Oswald:wght@300;400&display=swap" rel="stylesheet">
<style>
:root{
  --stage:#0b0b0b;
  --green:#138a68;
  --green-dark:#0f6f54;
  --ink:#1d1f22;
  --carousel:#232428;
  --paper:#ffffff;
  --mist:#e4e4e4;
  --footer:#3f3f3f;
  --footer-text:#9a9a9a;
  --footer-link:#20a981;
}
*{box-sizing:border-box;margin:0;padding:0}
html,body{width:1200px;height:1200px;overflow:hidden;background:var(--stage)}
body{font-family:"Arimo",Arial,sans-serif;position:relative}
.page{position:absolute;left:353px;top:34px;width:494px;height:1132px;background:var(--paper);overflow:hidden}
.abs{position:absolute}

/* header */
.site-header{left:0;top:0;width:494px;height:34px;background:var(--paper)}
.brand{left:35px;top:10px;font-family:"Archivo Black",sans-serif;font-size:10px;color:var(--ink);letter-spacing:.4px;line-height:1;white-space:nowrap}
.brand-tag{left:36px;top:22px;font-size:3.6px;letter-spacing:.9px;color:var(--ink);text-transform:uppercase;white-space:nowrap}
.nav{right:14px;top:15px;display:flex;gap:16px;font-size:6px;color:#444;letter-spacing:.2px}
.nav .active::before{content:"";display:inline-block;width:4px;height:5px;background:var(--green);margin-right:3px;vertical-align:-0.5px}

/* hero */
.hero{left:0;top:34px;width:494px;height:237px;background:linear-gradient(90deg,#2c2e31,#1d1e20);overflow:hidden}
.hero-photo{left:220px;top:0;width:274px;height:237px;background:radial-gradient(ellipse at 40% 45%,#b07a55 0%,#7a4b2c 35%,#3a2a22 70%,#1e1e20 100%)}
.hero-title{left:35px;top:68px;color:#fff;line-height:1}
.hero-title .thin{font-family:"Arimo",sans-serif;font-weight:400;font-size:28px;letter-spacing:-.5px;display:block}
.hero-title .bold{font-family:"Archivo Black",sans-serif;font-size:20.5px;letter-spacing:.2px;display:block;margin-top:1px}
.hero-copy{left:37px;top:128px;width:172px;color:#fff;font-size:7px;font-weight:700;line-height:1.38}

/* about */
.about{left:0;top:271px;width:494px;height:194px;background:var(--paper)}
.about-band{left:0;top:4px;width:494px;height:190px;background:var(--green)}
.about-title{left:34px;top:40px;width:426px;height:20px;border-radius:10px;background:#1e2a26;color:#fff;font-family:"Archivo Black",sans-serif;font-size:11.5px;text-align:center;line-height:20px;white-space:nowrap}
.about-copy{left:90px;top:72px;width:314px;color:#fff;font-size:7px;font-weight:700;text-align:center;line-height:1.2}
.about-copy p+p{margin-top:8px}
.btn-more{left:214px;top:163px;width:68px;height:18px;background:var(--ink);color:#fff;font-size:7px;font-weight:700;text-align:center;line-height:18px;border-radius:3px;letter-spacing:.3px}

/* gallery carousel */
.gallery{left:0;top:465px;width:494px;height:153px;background:var(--carousel)}
.shot{background:linear-gradient(135deg,#5a5a5a,#bdbdbd 45%,#7a7a7a 70%,#3e3e3e)}
.shot.far{opacity:.55}
.shot.center{background:linear-gradient(135deg,#8c8c8c,#e8e8e8 40%,#a9a9a9 70%,#f2f2f2)}
.arrow{width:38px;height:59px;top:513px;border-radius:30px;background:#4a4b4e}

/* booking */
.book-band{left:0;top:618px;width:494px;height:28px;background:var(--green);color:#fff;font-family:"Archivo Black",sans-serif;font-size:14px;text-align:center;line-height:29px}
.services{left:0;top:646px;width:494px;height:194px;background:var(--mist);z-index:2;overflow:visible}
.service{position:absolute;left:0;width:494px;text-align:center;font-family:"Oswald",sans-serif;font-weight:300;font-size:16px;color:var(--green);letter-spacing:.3px;line-height:20px}

/* testimonials */
.testimonials{left:0;top:840px;width:494px;height:104px;background:var(--paper)}
.review{position:absolute;left:62px;display:flex;gap:5px;font-size:4.6px;line-height:10px}
.review .who{width:28px;color:var(--green);white-space:nowrap}
.review .says{width:322px;color:#333;text-transform:uppercase}

/* footer */
.site-footer{left:0;top:944px;width:494px;height:188px;background:var(--footer);color:var(--footer-text)}
.foot-col{position:absolute;border-top:1px solid #666;padding-top:4px}
.foot-col h4{font-weight:400;font-size:5.6px;color:#aaa;margin-bottom:3px}
.foot-col p{font-size:3.9px;line-height:1.5;font-style:italic}
.foot-col .links{font-style:normal;color:var(--footer-link)}
.store{position:absolute;top:118px;width:44px;height:15px;background:#111;border:0.6px solid #888;border-radius:2px}
.legal{left:0;top:1112px;width:494px;text-align:center;font-size:4.6px;color:#cfcfcf;white-space:nowrap}
</style>
</head>
<body>
<main class="page">

  <header class="site-header abs">
    <div class="brand abs">CURL RADIANT</div>
    <div class="brand-tag abs">through &amp; through</div>
    <nav class="nav abs">
      <span class="active">BUTTON</span><span>BUTTON2</span><span>BUTTON2</span><span>BUTTON2</span><span>BUTTON2</span>
    </nav>
  </header>

  <section class="hero abs">
    <svg class="abs" style="left:0;top:0" width="494" height="237" viewBox="0 0 494 237">
      <polygon points="80,237 130,237 340,0 290,0" fill="#1b5e4a" opacity=".75"/>
      <polygon points="130,237 175,237 380,0 340,0" fill="#163f34" opacity=".7"/>
      <polygon points="20,170 60,237 110,237 50,150" fill="#3a3c40" opacity=".6"/>
    </svg>
    <div class="hero-photo abs" role="img" aria-label="Portrait of a woman with voluminous curly hair"></div>
    <h1 class="hero-title abs"><span class="thin">BEAUY IS</span><span class="bold">EVERYWHERE</span></h1>
    <p class="hero-copy abs">Lorem Ipsum is simply dummy text of the printing and typesetting industry. Dummy text of the printing and typesetting industry.</p>
  </section>

  <section class="about abs">
    <div class="about-band abs"></div>
    <svg class="abs" style="left:232px;top:3px" width="32" height="18" viewBox="0 0 32 18"><polygon points="0,0 32,0 16,16" fill="#ffffff"/><polygon points="4,0 28,0 16,12" fill="#0f6f54"/></svg>
    <h2 class="about-title abs">CURL RADIANT THROUGH &amp; THROUGH BY MARISOL B.</h2>
    <div class="about-copy abs">
      <p>Creative. Classic. Distinguished. These are just a few attributes that Marisol embodies. received in depth training from Harbor Academy of Hair Design, where I had the opportunity to pair my experience with advanced technical training. My passion for art and design has given me the opportunity to express myself through hair design. I also stay abreast of current trends through industry events, hair shows, and continuing education so that I can offer my clients the best services in hair care, style, and extensions.</p>
      <p>I've spent the last five years perfecting my method of installing extensions which offers my clients a ... (more)</p>
    </div>
    <div class="btn-more abs">VIEW MORE</div>
  </section>

  <section class="gallery abs" aria-label="Gallery">
    <div class="shot far abs" style="left:40px;top:30px;width:58px;height:92px" role="img" aria-label="Curly hairstyle photo"></div>
    <div class="shot far abs" style="left:396px;top:30px;width:58px;height:92px" role="img" aria-label="Curly hairstyle photo"></div>
    <div class="shot abs" style="left:98px;top:20px;width:88px;height:111px" role="img" aria-label="Curly hairstyle photo"></div>
    <div class="shot abs" style="left:308px;top:20px;width:88px;height:111px" role="img" aria-label="Curly hairstyle photo"></div>
    <div class="shot center abs" style="left:185px;top:15px;width:123px;height:123px" role="img" aria-label="Featured curly hairstyle photo"></div>
  </section>
  <div class="arrow abs" style="left:-19px"></div>
  <div class="arrow abs" style="left:475px"></div>
  <svg class="abs" style="left:8px;top:533px" width="10" height="20" viewBox="0 0 10 20"><polyline points="9,1 1,10 9,19" fill="none" stroke="#ddd" stroke-width="2.4"/></svg>
  <svg class="abs" style="left:476px;top:533px" width="10" height="20" viewBox="0 0 10 20"><polyline points="1,1 9,10 1,19" fill="none" stroke="#ddd" stroke-width="2.4"/></svg>

  <h2 class="book-band abs">BOOK AN APPOINTMENT</h2>

  <section class="services abs">
    <div class="service" style="top:12px">BASIC SERVICES</div>
    <div class="service" style="top:61px">COLOR SERVICES</div>
    <div class="service" style="top:112px">EXTENSIONS</div>
    <div class="service" style="top:162px">STRAITENING SERVICES</div>
    <svg class="abs" style="left:0;top:0" width="494" height="212" viewBox="0 0 494 212">
      <g fill="none" stroke="#bdbdbd" stroke-width="2.4">
        <polyline points="0,44 230,44 247,58 264,44 494,44"/>
        <polyline points="0,93 230,93 247,107 264,93 494,93"/>
        <polyline points="0,143 230,143 247,157 264,143 494,143"/>
        <polyline points="0,193 230,193 247,207 264,193 494,193"/>
      </g>
      <polygon points="232,46 262,46 247,57" fill="#e4e4e4"/>
      <polygon points="232,95 262,95 247,106" fill="#e4e4e4"/>
      <polygon points="232,145 262,145 247,156" fill="#e4e4e4"/>
      <polygon points="232,195 262,195 247,206" fill="#e4e4e4"/>
    </svg>
  </section>

  <section class="testimonials abs">
    <div class="review" style="top:26px"><div class="who">RENATA B.<br>2/09/16</div><div class="says">"I have been looking for a stylist since I moved to Dallas for 7 years. I noticed a young ladys hair and she gave me Marisol information. I love my hair. She does an amazing job. Always leave satisfied!!!"</div></div>
    <div class="review" style="top:53px"><div class="who">RENATA B.<br>2/09/16</div><div class="says">"I never leave her shop disappointed! She's miracle worker to say the least ;)"</div></div>
  </section>

  <footer class="site-footer abs">
    <div class="foot-col" style="left:72px;top:39px;width:237px"><h4>ABOUT</h4><p>TrimNook is the online home for beauty &amp; wellness pros and their clients. Professionals can display their work, connect with new and returning clients, and grow their business. Clients can discover new services and providers, book appointments online, and get inspired. <span class="links">learn more »</span></p></div>
    <div class="foot-col" style="left:331px;top:39px;width:93px"><h4>MEDIA</h4><p class="links">Beauty Blog · Press · Stories · Videos</p></div>
    <div class="foot-col" style="left:72px;top:82px;width:237px"><h4>FEATURED CITIES</h4><p class="links">Northgate · Lakeview · Riverside · Harbor City · Pine Hollow · Westfield · Maple Ridge · Sunvale · Brookport · Eastmoor · Cedar Falls · Granite Bay · Oakmont · Silver Lake · Fairhaven · Willow Park · Bayshore · Highmeadow · Stonebridge · Ashford · Kingsley · Clearwater · Redmont · Elmwood</p></div>
    <div class="foot-col" style="left:331px;top:82px;width:54px"><h4>TALK TO US</h4><p class="links">hello@trimnook.example<br>TrimNook Help Desk</p></div>
    <div class="store" style="left:331px"></div>
    <div class="store" style="left:377px"></div>
  </footer>
  <div class="legal abs">© 2016 TRIMNOOK, INC. ALL RIGHTS RESERVED. FIND PROFESSIONALS GET LISTED TEAM JOBS TERMS PRIVACY SITEMAP FEED POSTS CIRCLE</div>

</main>
</body>
</html>
```